Varolta Business Card

I am looking for a business card design for a start-up company called Varolta Group. This is a management consultancy focused on sales, marketing, sales management, product management and AGILE software development. Our primary customers are $1M to $50M in revenue.

Varolta is the Italian word for "slope."

The path from $0 to $50M has many different growth stages associated with it. Each one having a significant slope to the next plateau. Our expertise helps our customers ascend each of those slopes. We bring experience, successful track-records in growing companies, best practices and a dive-in and roll-up your sleeves mentality. We are not sitting at base camp shouting instructions, we are right there with you, on the climb.

Industry/Entity Type

Business

```html
<!DOCTYPE html>
<html lang="en">
<head>
<meta charset="utf-8">
<title>Varolta Business Card</title>
<link href="https://fonts.googleapis.com/css2?family=Questrial&family=Roboto:wght@300&display=swap" rel="stylesheet">
<style>
  :root {
    --stage: #000000;
    --card: #ffffff;
    --ink: #5f6a70;
    --ink-soft: #7d878c;
    --blue-deep: #0a4d8c;
    --blue-bright: #12a6e4;
    --green-deep: #3f7a2a;
    --green-bright: #9ccb3b;
    --mark: #2f7fb8;
  }
  * { margin: 0; padding: 0; box-sizing: border-box; }
  html, body { width: 1200px; height: 1000px; overflow: hidden; background: var(--stage); }
  .stage { position: relative; width: 1200px; height: 1000px; }
  .card {
    position: absolute; top: 218px; width: 320px; height: 543px;
    background: var(--card); overflow: hidden; color: var(--ink);
    font-family: "Roboto", Arial, sans-serif; font-weight: 300;
  }
  .card--back { left: 213px; }
  .card--front { left: 626px; }

  .brand { position: absolute; display: flex; align-items: center; }
  .brand__dot { border-radius: 50%; background: var(--mark); flex: none; }
  .brand__name { font-family: "Questrial", Arial, sans-serif; font-weight: 400; color: var(--ink); }

  .card--back .brand { left: 0; right: 0; top: 182px; flex-direction: column; }
  .card--back .brand__dot { width: 92px; height: 92px; }
  .card--back .brand__name { font-size: 52px; line-height: 1; margin-top: 8px; letter-spacing: -0.5px; }

  .links { position: absolute; left: 83px; top: 457px; list-style: none; font-size: 15.5px; line-height: 21px; color: var(--ink-soft); }
  .links li { display: flex; align-items: center; }
  .links__marker { width: 12px; height: 12px; background: var(--mark); margin-right: 7px; flex: none; }

  .hero { position: absolute; left: 0; top: 0; width: 320px; height: 275px; display: block; }

  .card--front .brand { left: 46px; top: 268px; }
  .card--front .brand__dot { width: 44px; height: 44px; margin-right: 10px; }
  .card--front .brand__name { font-size: 38px; line-height: 1; }

  .person { position: absolute; left: 49px; top: 340px; }
  .person__name { font-family: "Questrial", Arial, sans-serif; font-size: 20px; line-height: 24px; color: var(--ink); }
  .person__role { font-size: 15.5px; line-height: 18px; color: var(--ink-soft); }

  .details { position: absolute; left: 49px; font-size: 15.5px; line-height: 19px; color: var(--ink-soft); font-style: normal; }
  .details--address { top: 395px; }
  .details--contact { top: 463px; }
</style>
</head>
<body>
<main class="stage">
  <section class="card card--back" aria-label="Card back">
    <div class="brand">
      <span class="brand__dot"></span>
      <span class="brand__name">Varolta</span>
    </div>
    <ul class="links">
      <li><span class="links__marker"></span>varoltagroup.com</li>
      <li><span class="links__marker"></span>Varolta Group</li>
      <li><span class="links__marker"></span>@varoltagroup</li>
    </ul>
  </section>

  <section class="card card--front" aria-label="Card front">
    <svg class="hero" viewBox="0 0 320 275" role="img" aria-label="Blue to green gradient band with a sloping curved edge">
      <defs>
        <linearGradient id="slope-fill" x1="0" y1="0.3" x2="1" y2="0.7">
          <stop offset="0" stop-color="var(--blue-deep)"/>
          <stop offset="0.35" stop-color="var(--blue-bright)"/>
          <stop offset="0.6" stop-color="var(--green-deep)"/>
          <stop offset="1" stop-color="var(--green-bright)"/>
        </linearGradient>
      </defs>
      <path d="M0 0 H320 V190 Q150 150 0 272 Z" fill="url(#slope-fill)"/>
    </svg>

    <div class="brand">
      <span class="brand__dot"></span>
      <span class="brand__name">Varolta</span>
    </div>

    <div class="person">
      <p class="person__name">Marco D. Ferrante</p>
      <p class="person__role">Managing Partner</p>
    </div>

    <address class="details details--address">
      Varolta Group, Inc.<br>
      2870 N. Ridge Avenue, Suite 410<br>
      Denver, CO 80205
    </address>

    <address class="details details--contact">
      office: +1 303 555 0142<br>
      mobile: +1 303 555 0187<br>
      marco.ferrante@varolta.email
    </address>
  </section>
</main>
</body>
</html>
```